Bookcover: Lessons From the Silent Orchard

I am publishing a super-low-cost innovation book for €4,99 on Bravolo Self Release to help everyone become a great innovator: young ambitious people without college education nor a big budget. Do you want to help me?

Brief:
Design a book cover 1600 x 2560 pixels for BSR.
Main title: Lessons From the Silent Orchard
Sub title: mindset - insights - skills & tools
Author: Maarten de Klerk
Design: captive, and appealing to everyone
Target Group: young ambitious people without college education

For bravolo please format the height/width ratio of 1.6:1

```html
<!DOCTYPE html>
<html lang="en">
<head>
<meta charset="utf-8">
<title>Lessons From the Silent Orchard – Book Cover</title>
<link rel="stylesheet" href="https://fonts.googleapis.com/css2?family=Poppins:wght@600;700&family=Staatliches&display=swap">
<style>
  :root {
    --page-bg: #e9e9e9;
    --night-top: #0b1a2c;
    --night-mid: #10182a;
    --night-low: #050608;
    --glow-core: #fffbe6;
    --glow-bulb: #d9d49a;
    --glow-warm: #8a3a28;
    --glow-dusk: #3a1d2a;
    --ink-light: #ffffff;
    --rule: rgba(255, 255, 255, 0.75);
  }

  * { margin: 0; padding: 0; box-sizing: border-box; }

  html, body {
    width: 1200px;
    height: 1144px;
    overflow: hidden;
    background: var(--page-bg);
  }

  .book-cover {
    position: absolute;
    left: 275px;
    top: 52px;
    width: 650px;
    height: 1040px;
    overflow: hidden;
    color: var(--ink-light);
    background: linear-gradient(180deg, var(--night-top) 0%, var(--night-mid) 40%, var(--night-low) 88%, #000 100%);
    text-align: center;
  }

  .cover-artwork {
    position: absolute;
    left: 0;
    top: 300px;
    width: 650px;
    height: 620px;
    background:
      radial-gradient(ellipse 150px 190px at 50% 52%, var(--glow-core) 0%, var(--glow-bulb) 45%, rgba(217, 212, 154, 0) 100%),
      radial-gradient(ellipse 330px 300px at 50% 55%, var(--glow-warm) 0%, var(--glow-dusk) 55%, rgba(16, 24, 42, 0) 100%),
      linear-gradient(180deg, rgba(0, 0, 0, 0) 0%, rgba(0, 0, 0, 0) 82%, #000 100%);
  }

  .title-block {
    position: absolute;
    left: 0;
    right: 0;
    top: 66px;
  }

  .title-lead {
    font-family: "Poppins", sans-serif;
    font-weight: 700;
    font-size: 18px;
    letter-spacing: 0.62em;
    padding-left: 0.62em;
    line-height: 1;
  }

  .title-main {
    font-family: "Staatliches", sans-serif;
    font-weight: 400;
    font-size: 138px;
    line-height: 0.82;
    letter-spacing: 0.01em;
    margin-top: 12px;
  }

  .title-main span { display: block; }

  .subtitle {
    display: inline-block;
    margin-top: 14px;
    padding: 7px 18px 6px;
    border-top: 1px solid var(--rule);
    border-bottom: 1px solid var(--rule);
    font-family: "Poppins", sans-serif;
    font-weight: 700;
    font-size: 21px;
    line-height: 1.2;
    text-transform: uppercase;
  }

  .author {
    position: absolute;
    left: 0;
    right: 0;
    top: 962px;
    font-family: "Poppins", sans-serif;
    font-weight: 600;
    font-size: 19px;
    letter-spacing: 0.5em;
    padding-left: 0.5em;
    text-transform: uppercase;
  }
</style>
</head>
<body>
  <main class="book-cover">
    <div class="cover-artwork" role="img" aria-label="Night sky full of stars above a forest; a silhouetted person stands on a hill inside a large glowing light bulb"></div>

    <header class="title-block">
      <p class="title-lead">LESSONS FROM THE</p>
      <h1 class="title-main"><span>SILENT</span><span>ORCHARD</span></h1>
      <p class="subtitle">Mindset – Insights – Skills &amp; Tools</p>
    </header>

    <p class="author">Maarten de Klerk</p>
  </main>
</body>
</html>
```